BSWC Steadwell Foot Health Care

Steadwell Foot Health Care guarantees to treat your foot problems in one visit or we will provide a free treatment session to you until you are completely satisfied.

10% discount for all new patients!

Mobile foot care at home!

Professional and fully qualified and insured foot health care practitioner

Expert advice

How to care for your feet

Treatments; Diabetic foot health, Corns, Callouses, Fungal Infections, Verrucas, Cracked Heels, Ingrowing Toenails, Ball of foot pain and Heel pain.

```html
<!DOCTYPE html>
<html lang="en">
<head>
<meta charset="utf-8">
<title>BSWC Steadwell Foot Health Care – Flyer</title>
<link href="https://fonts.googleapis.com/css2?family=Jost:wght@400;500;600&family=Gelasio:wght@400;700&display=swap" rel="stylesheet">
<style>
  :root {
    --backdrop: #2a2a2a;
    --paper: #ffffff;
    --paper-shade: #f0f0f0;
    --pink: #f08cbc;
    --pink-soft: #f7c3dc;
    --red: #e3151f;
    --ink: #111111;
    --skin-light: #fbe6dc;
    --skin-mid: #f1c9b6;
  }
  * { box-sizing: border-box; margin: 0; padding: 0; }
  html, body { width: 900px; height: 1200px; overflow: hidden; }
  body { background: var(--backdrop); font-family: "Jost", sans-serif; color: var(--ink); position: relative; }

  .flyer {
    position: absolute; left: 110px; width: 685px; height: 487px;
    background: linear-gradient(180deg, var(--paper) 0%, var(--paper-shade) 100%);
    overflow: hidden;
  }
  .flyer--front { top: 73px; }
  .flyer--back { top: 650px; }

  /* Front */
  .front-header {
    position: absolute; left: 0; top: 20px; width: 440px; height: 50px;
    background: var(--pink); color: #fff; font-weight: 400;
    font-family: "Gelasio", serif; font-size: 30px; line-height: 50px; padding-left: 25px;
  }
  .hero-photo {
    position: absolute; left: 315px; top: -60px; width: 550px; height: 550px; border-radius: 50%;
    border: 9px solid var(--pink);
    background: radial-gradient(circle at 45% 55%, var(--skin-light) 0%, var(--skin-mid) 55%, #fff 90%);
  }
  .front-copy { position: absolute; left: 25px; top: 98px; width: 300px; }
  .front-copy .intro { font-size: 15px; line-height: 26px; white-space: nowrap; }
  .front-copy .discount { color: var(--red); font-size: 33px; line-height: 44px; }
  .front-copy .audience { font-size: 25px; line-height: 52px; }
  .front-copy .cta { font-size: 22px; line-height: 48px; }
  .front-copy .phone { color: var(--red); font-size: 36px; line-height: 42px; letter-spacing: 1px; }
  .thumb-circle {
    position: absolute; top: 365px; width: 92px; height: 92px; border-radius: 50%;
    border: 5px solid var(--pink);
    background: radial-gradient(circle, var(--skin-light) 30%, var(--skin-mid) 100%);
  }
  .thumb-circle--heel { left: 41px; }
  .thumb-circle--feet { left: 166px; }

  /* Back */
  .back-intro {
    position: absolute; left: 0; top: 22px; width: 100%; text-align: center;
    font-family: "Gelasio", serif; font-size: 15px; line-height: 25px;
  }
  .back-intro .accent { color: var(--red); }
  .back-intro strong { font-weight: 700; }
  .wave { position: absolute; left: 0; top: 0; width: 685px; height: 487px; }
  .service-copy { position: absolute; left: 25px; top: 168px; width: 430px; font-size: 12.5px; line-height: 19px; }
  .result-photo {
    position: absolute; left: 547px; top: 173px; width: 112px; height: 112px; border-radius: 50%;
    border: 3px solid var(--red);
    background: linear-gradient(90deg, #9b8a80 0%, #c9b2a4 48%, #fff 49%, #fff 51%, #e2c2b0 52%, #c79c86 100%);
    font-size: 10px; font-weight: 600;
  }
  .result-photo span { position: absolute; top: 48px; }
  .result-photo .before { left: 4px; }
  .result-photo .after { right: 10px; }
  .care-tab {
    position: absolute; left: 0; top: 280px; width: 228px; height: 37px;
    background: var(--pink); color: #fff; border-radius: 0 20px 20px 0; font-weight: 400;
    font-family: "Gelasio", serif; font-size: 16px; line-height: 37px; padding-left: 16px;
  }
  .treatments { position: absolute; left: 25px; top: 325px; width: 650px; font-size: 13px; line-height: 17px; }
  .treatments .offer { color: var(--red); font-weight: 600; font-size: 15px; }
  .treatment-photo {
    position: absolute; top: 384px; width: 84px; height: 50px; border: 2px solid var(--red);
    background: linear-gradient(135deg, #c9a08a 0%, #6b4a3a 60%, #2e2420 100%);
  }
  .treatment-photo--1 { left: 187px; }
  .treatment-photo--2 { left: 300px; }
  .treatment-photo--3 { left: 413px; }
  .booking-band {
    position: absolute; left: 0; bottom: 0; width: 100%; height: 42px;
    background: var(--pink); color: #fff; font-size: 12px; line-height: 42px; padding-left: 17px;
  }
  .booking-band strong { font-size: 13px; font-weight: 600; }
</style>
</head>
<body>
  <section class="flyer flyer--front">
    <div class="hero-photo" role="img" aria-label="Photograph of a pair of bare feet held in a woman's hands"></div>
    <h1 class="front-header">Feet Street News!!!</h1>
    <div class="front-copy">
      <p class="intro">Newly arrived mobile foot care at<br>home is in now available in your area</p>
      <p class="discount">10% Discounts</p>
      <p class="audience">for all new patients</p>
      <p class="cta">CALL NOW to register</p>
      <p class="phone">07700900412</p>
    </div>
    <div class="thumb-circle thumb-circle--heel" role="img" aria-label="Photograph of a sore heel"></div>
    <div class="thumb-circle thumb-circle--feet" role="img" aria-label="Photograph of feet at rest"></div>
  </section>

  <section class="flyer flyer--back">
    <svg class="wave" viewBox="0 0 685 487" aria-hidden="true">
      <path d="M0,175 C110,125 250,110 380,140 C500,168 600,172 685,160 L685,176 C590,198 470,196 360,168 C240,140 110,150 0,200 Z" fill="var(--pink)"/>
      <path d="M0,200 C110,150 240,140 360,168 C470,196 590,198 685,176 L685,200 C580,218 460,214 350,190 C230,164 110,172 0,215 Z" fill="var(--pink-soft)" opacity="0.6"/>
    </svg>
    <p class="back-intro">
      <span class="accent">BSWC S</span>teadwell <span class="accent">F</span>oot Health <span class="accent">C</span>are <strong>Guarantees to treat your foot problems in one visit</strong><br>
      or we will provide a free treatment session to you until you’re completely satisfied.<br>
      We will conveniently visit you in your own home or place of work which<br>
      ever you find more comfortable.
    </p>
    <p class="service-copy">From as little as 30 per treatment<br>session our fully qualified and insured Foot<br>Health Care Practitioner will immediately bring you<br>pain relief while also offering you professional expert advice on<br>how to care for your feet and keep them looking good all year round.</p>
    <div class="result-photo" role="img" aria-label="Before and after photograph of a treated heel"><span class="before">Before</span><span class="after">After</span></div>
    <h2 class="care-tab">How to care for your feet</h2>
    <p class="treatments">Specialising in Diabetic foot health and Elderly foot care <span class="offer">10% off TREATMENTS</span><br>Corns, Calluses, Fungal infections, Verruca’s, Cracked heels, In growing toenails, Ball of foot pain,<br>Heel pain and Diabetic Foot Health.</p>
    <div class="treatment-photo treatment-photo--1" role="img" aria-label="Photograph of a foot treatment"></div>
    <div class="treatment-photo treatment-photo--2" role="img" aria-label="Photograph of toenail care"></div>
    <div class="treatment-photo treatment-photo--3" role="img" aria-label="Photograph of a practitioner at work"></div>
    <p class="booking-band"><strong>Call NOW!!! 07700900412</strong> to book an appointment with BSWC Ms R J Hale DipCFHP Foot Health care Practitioner</p>
  </section>
</body>
</html>
```